Orthodontic Office Needs New Stationary

We have recently renovated our office and are opening a second location. We need new stationary/branding to go with our new look. We like our logo, but are open to changing the colors to match the office look/feel more.

```html
<!DOCTYPE html>
<html lang="en">
<head>
<meta charset="utf-8">
<title>Harlow &amp; Vance Orthodontics – Presentation Folder</title>
<link rel="stylesheet" href="https://fonts.googleapis.com/css2?family=Open+Sans:wght@400;600&display=swap">
<style>
  :root {
    --backdrop: #d9d9da;
    --paper: #ffffff;
    --paper-shade: #f1f1f2;
    --brand-blue: #235874;
    --text-grey: #555a5e;
    --mark-faint: #e8e8e9;
  }
  * { margin: 0; padding: 0; box-sizing: border-box; }
  html, body { width: 1200px; height: 847px; overflow: hidden; }
  body {
    background: var(--backdrop);
    display: flex;
    align-items: center;
    justify-content: center;
  }
  .folder-spread {
    display: flex;
    box-shadow: 0 10px 30px rgba(0,0,0,0.18);
  }
  .folder-panel {
    width: 440px;
    height: 580px;
    position: relative;
  }
  .back-cover {
    background: linear-gradient(90deg, var(--paper-shade), var(--paper) 45%, var(--paper-shade));
    border-right: 1px solid #e2e2e3;
  }
  .front-cover {
    background: linear-gradient(90deg, var(--paper), var(--paper) 60%, var(--paper-shade));
  }
  .watermark-placeholder {
    position: absolute;
    left: 50%;
    top: 44%;
    transform: translate(-50%, -50%);
    width: 230px;
    height: 230px;
    border: 4px solid var(--mark-faint);
    border-radius: 50%;
  }
  .contact-block {
    position: absolute;
    left: 0;
    right: 0;
    bottom: 46px;
    text-align: center;
    font-family: "Open Sans", sans-serif;
    font-size: 10px;
    line-height: 1.55;
    color: var(--text-grey);
  }
  .contact-name {
    font-weight: 600;
    color: var(--brand-blue);
    font-size: 10.5px;
  }
  .contact-row { display: flex; justify-content: center; gap: 14px; }
  .contact-item { display: inline-flex; align-items: center; gap: 4px; }
  .contact-item svg { width: 10px; height: 10px; fill: var(--brand-blue); }
  .brand-name {
    position: absolute;
    left: 0;
    right: 0;
    top: 36%;
    text-align: center;
    font-family: "Open Sans", sans-serif;
    font-weight: 600;
    font-size: 24px;
    color: var(--brand-blue);
  }
  .front-web {
    position: absolute;
    left: 0;
    right: 0;
    bottom: 40px;
    text-align: center;
    font-family: "Open Sans", sans-serif;
    font-size: 12px;
    color: var(--brand-blue);
  }
</style>
</head>
<body>
  <main class="folder-spread">
    <section class="folder-panel back-cover">
      <div class="watermark-placeholder" role="img" aria-label="Faint brand mark watermark"></div>
      <div class="contact-block">
        <p class="contact-name">Harlow &amp; Vance Orthodontic</p>
        <p>48 Maple Crest Road, Lakeview, ON K2M 4R7</p>
        <p class="contact-row">
          <span class="contact-item">
            <svg viewBox="0 0 24 24"><path d="M6.6 10.8a15.1 15.1 0 0 0 6.6 6.6l2.2-2.2c.3-.3.7-.4 1-.2 1.1.4 2.3.6 3.6.6.6 0 1 .4 1 1V20c0 .6-.4 1-1 1A17 17 0 0 1 3 4c0-.6.4-1 1-1h3.5c.6 0 1 .4 1 1 0 1.3.2 2.5.6 3.6.1.3 0 .7-.2 1z"/></svg>
            +15550142386
          </span>
          <span class="contact-item">
            <svg viewBox="0 0 24 24"><path d="M2 5h20v14H2zm2 2v.3l8 6 8-6V7l-8 6z"/></svg>
            info@harlowvance.com
          </span>
          <span class="contact-item">
            <svg viewBox="0 0 24 24"><path d="M12 2a10 10 0 1 0 0 20 10 10 0 0 0 0-20zm0 2a8 8 0 0 1 7.7 6H4.3A8 8 0 0 1 12 4zM4 12h16a8 8 0 0 1-.3 2H4.3A8 8 0 0 1 4 12zm.9 4h14.2A8 8 0 0 1 12 20a8 8 0 0 1-7.1-4z"/></svg>
            www.harlowvance.com
          </span>
        </p>
      </div>
    </section>
    <section class="folder-panel front-cover">
      <p class="brand-name">Harlow &amp; Vance Orthodontics</p>
      <p class="front-web">www.harlowvance.com</p>
    </section>
  </main>
</body>
</html>
```